Business card design needed

Our company background is that we provides transfers to and from the airport, social & corporate events, weddings.
We are also available for charter for birthday party, wine tastings, concerts, anniversary, school balls etc.
Our business cards have to reflect that we have a professional company, they are our first contact and have to stand out from the other 'players' in the market.

Industry/Entity Type

School

Contact Information for Business Card

VESTAR PTH, Teodor & Marguerite, mob: 0427 381 592, PO Box 284, Harlow Bay WA 6172, ABN 52 614 203 178, Lic 7169/2058,

Requirements
Must have
• Telephone number: 0427 381 592
Website: www.VESTARPTH.com.au
postal address: PO Box 284, Harlow Bay WA 6172
Licences: Lic 7169/2058

***If using the new photo (one with the bus and buildings behind it), if possible can the buildings be cropped out. Thanks
Nice to have
• would be nice to have the pics of the vehicle(s), preferred the Vel on the card but not too fussed.
Should not have
• Picture of vehicle we don't have in our fleet. (We ONLY have the Velarions and Murako Densa mini bus)

```html
<!DOCTYPE html>
<html lang="en">
<head>
<meta charset="utf-8">
<title>Vestar Luxury Car &amp; Coach — Business Card</title>
<link rel="stylesheet" href="https://fonts.googleapis.com/css2?family=Comfortaa:wght@400&display=swap">
<style>
  :root {
    --card-bg-deep: #3f1a5c;
    --card-bg: #4d2470;
    --panel: rgba(122, 78, 158, 0.55);
    --text-light: #ffffff;
    --sedan-light: #d9d6cf;
    --sedan-dark: #8c877d;
    --van-light: #f4f4f4;
    --van-dark: #a9a9ad;
  }
  * { margin: 0; padding: 0; box-sizing: border-box; }
  html, body {
    width: 1200px;
    height: 742px;
    overflow: hidden;
    background: var(--card-bg-deep);
  }
  .business-card {
    position: relative;
    width: 1200px;
    height: 742px;
    overflow: hidden;
    background: radial-gradient(ellipse at 55% 50%, var(--card-bg) 0%, var(--card-bg-deep) 100%);
    font-family: "Comfortaa", sans-serif;
    font-weight: 400;
    color: var(--text-light);
  }
  .brand-panel {
    position: absolute;
    left: 30px;
    top: 30px;
    width: 581px;
    height: 284px;
    border-radius: 10px;
    background: var(--panel);
    display: flex;
    flex-direction: column;
    justify-content: center;
    align-items: center;
    text-align: center;
    gap: 18px;
  }
  .brand-name {
    font-size: 92px;
    font-weight: 400;
    line-height: 1;
  }
  .brand-tagline {
    font-size: 40px;
    font-weight: 400;
    line-height: 1;
  }
  .vehicle-photo {
    position: absolute;
    border-radius: 10px;
  }
  .vehicle-photo--sedan {
    left: 622px;
    top: 4px;
    width: 565px;
    height: 347px;
    background: linear-gradient(180deg, var(--sedan-light) 0%, var(--sedan-dark) 70%, #3b3a38 100%);
  }
  .vehicle-photo--van {
    left: 0;
    top: 320px;
    width: 494px;
    height: 422px;
    border-radius: 0 10px 0 0;
    background: linear-gradient(180deg, var(--van-light) 0%, var(--van-dark) 75%, #3a3a3c 100%);
  }
  .contact-panel {
    position: absolute;
    left: 503px;
    top: 394px;
    width: 684px;
    height: 321px;
    border-radius: 10px;
    background: var(--panel);
    text-align: right;
    padding: 36px 24px 0 0;
  }
  .contact-line {
    font-size: 34px;
    line-height: 47px;
    white-space: nowrap;
  }
  .contact-line--names { margin-bottom: 12px; }
  .contact-line--licence { margin-top: 12px; }
</style>
</head>
<body>
  <main class="business-card">
    <section class="brand-panel">
      <h1 class="brand-name">Vestar</h1>
      <p class="brand-tagline">Luxury Car &amp; Coach</p>
    </section>

    <div class="vehicle-photo vehicle-photo--sedan" role="img" aria-label="Photo of the silver Velarion luxury sedan, front view"></div>
    <div class="vehicle-photo vehicle-photo--van" role="img" aria-label="Photo of the white Murako Densa mini bus, front three-quarter view"></div>

    <section class="contact-panel">
      <p class="contact-line contact-line--names">Teodor &amp; Marguerite</p>
      <p class="contact-line">0427 381 592</p>
      <p class="contact-line">www.VESTARPTH.com.au</p>
      <p class="contact-line">PO Box 284, Harlow Bay WA 6172</p>
      <p class="contact-line contact-line--licence">Lic 7169/2058</p>
    </section>
  </main>
</body>
</html>
```